I need a front and back cover and spine design for a self help book. The complete title is BRIGHT PATH - Unlocking the Golden Key for Vigor & Contentment. This book is based on my own personal health journey during the pandemic, as well as my personal experience as a certified nutritional therapist and expert in the alkaline ionized water industry. This book is a practical approach of customizing a lifestyle based on a combination of popular diets and provides easy to understand definitions for some of the hottest health buzz words being used today. The cover should convey inspiration for a person to make a positive change, while also being visually inviting.
Updates

Need extra days to review

Target Market(s)

18+, people unhappy with thier health

Industry/Entity Type

health and wellness, self help

Colors
0054AA
0677BA
7BADD7
CADEEF
E8F1F8
00AB8E
00BBA5
67D7C9
C6EFE9
E9F9F6
EB3D1F
EC4F4E
F09395
F8D3D4
FCEDEE
6B429C
8869AF
B7A5CE
E3DAEB
F3F0F8

Requirements
Must have
• I'd like the back cover to have my before (47 years old) and after (54 years old) pcture that has been uploaded, along with the following text: Martin R. Vellacott has been a successful businessman, a business consultant, a published writer, an Adult Continuing Education Instructor and is currently a globally recognized expert in the Alkaline Water Industry and a Certified Nutritional Therapist. During his own health journey he has discovered the “Golden Key” for health and happiness and wants to let other people struggling with health, weight and happiness issues know that they are not alone and that is never too late to make a positive change in your life. His easy to understand advice is derived from a combination of over a decade of in-depth research, academic study and personal experience and now, at 54 years old, he is in the best shape of his life and hopes to inspire others to take control of their lives and live life to the fullest.
Nice to have
• Cover should have my name Martin R. Vellacott, with the following text appearing below my name: HYDRATION EXPERT & CERTIFIED NUTRITIONAL THERAPIST

```html
<!DOCTYPE html>
<html lang="en">
<head>
<meta charset="utf-8">
<title>Bright Path – Front Cover</title>
<link rel="stylesheet" href="https://fonts.googleapis.com/css2?family=Fredoka:wght@600&family=Fjalla+One&display=swap">
<style>
  :root {
    --cream: #e6dfc5;
    --navy: #1f3a5c;
    --band-red: #d93a30;
    --band-orange: #e9a23b;
    --band-green: #8aa95b;
    --leaf-green: #4f9a4a;
    --leaf-blue: #1f5e96;
    --petal-red: #cf2a2a;
    --petal-orange: #eea43a;
    --canvas-bg: #e9e5cf;
  }
  * { margin: 0; padding: 0; box-sizing: border-box; }
  html, body { width: 781px; height: 1200px; overflow: hidden; background: var(--canvas-bg); }
  .cover {
    position: relative;
    width: 781px;
    height: 1200px;
    overflow: hidden;
  }
  .cover-art { position: absolute; inset: 0; width: 781px; height: 1200px; }
  .title {
    position: absolute;
    left: 0; right: 0;
    text-align: center;
    font-family: "Fredoka", "Varela Round", sans-serif;
    font-weight: 600;
    color: var(--cream);
    line-height: 1;
    text-shadow: 2px 3px 4px rgba(0,0,0,0.45);
  }
  .title-line-one { top: 150px; font-size: 190px; letter-spacing: -2px; }
  .title-line-two { top: 420px; font-size: 280px; letter-spacing: -4px; }
  .subtitle-band {
    position: absolute;
    font-family: "Fjalla One", sans-serif;
    color: var(--navy);
    text-align: center;
    white-space: nowrap;
    line-height: 1;
  }
  .subtitle-primary {
    left: 60px; top: 781px; width: 686px; height: 57px;
    background: var(--band-red);
    font-size: 45px; padding-top: 4px; letter-spacing: 1px;
  }
  .subtitle-secondary {
    left: 97px; top: 849px; width: 612px; height: 55px;
    background: var(--band-orange);
    font-size: 45px; padding-top: 3px; letter-spacing: 1px;
  }
  .author-name {
    position: absolute;
    left: 0; right: 0; top: 1022px;
    text-align: center;
    font-family: "Fjalla One", sans-serif;
    font-size: 58px;
    letter-spacing: 3px;
    color: var(--cream);
    text-shadow: 2px 3px 3px rgba(0,0,0,0.5);
    line-height: 1;
  }
  .author-credentials {
    position: absolute;
    left: 49px; top: 1099px; width: 687px; height: 58px;
    background: var(--band-green);
    font-family: "Fjalla One", sans-serif;
    font-size: 27px;
    letter-spacing: 1.5px;
    color: var(--navy);
    text-align: center;
    padding-top: 13px;
    line-height: 1;
    white-space: nowrap;
  }
</style>
</head>
<body>
<main class="cover">
  <svg class="cover-art" viewBox="0 0 781 1200" role="img" aria-label="Painted illustration of bold red and orange flowers among green and blue leaves on a cream ground">
    <defs>
      <radialGradient id="greenField" cx="50%" cy="55%" r="65%">
        <stop offset="0" stop-color="#4f9a4a"/>
        <stop offset="0.7" stop-color="#6fae5a"/>
        <stop offset="1" stop-color="#dfe2c6"/>
      </radialGradient>
      <radialGradient id="redBloomTop" cx="0.5" cy="0.5" r="0.5">
        <stop offset="0" stop-color="#cf2a2a"/>
        <stop offset="0.7" stop-color="#cf2a2a" stop-opacity="0.8"/>
        <stop offset="1" stop-color="#cf2a2a" stop-opacity="0"/>
      </radialGradient>
      <radialGradient id="warmBloom" cx="0.5" cy="0.5" r="0.5">
        <stop offset="0" stop-color="#e0582c"/>
        <stop offset="0.6" stop-color="#d63a2a" stop-opacity="0.85"/>
        <stop offset="1" stop-color="#d63a2a" stop-opacity="0"/>
      </radialGradient>
      <radialGradient id="orangeBloom" cx="0.5" cy="0.5" r="0.5">
        <stop offset="0" stop-color="#eea43a"/>
        <stop offset="1" stop-color="#eea43a" stop-opacity="0"/>
      </radialGradient>
      <radialGradient id="blueLeaf" cx="0.5" cy="0.5" r="0.5">
        <stop offset="0" stop-color="#1f5e96"/>
        <stop offset="1" stop-color="#1f5e96" stop-opacity="0"/>
      </radialGradient>
    </defs>
    <rect width="781" height="1200" fill="url(#greenField)"/>
    <ellipse cx="110" cy="150" rx="160" ry="170" fill="url(#blueLeaf)"/>
    <ellipse cx="720" cy="700" rx="140" ry="260" fill="url(#blueLeaf)"/>
    <ellipse cx="80" cy="1050" rx="150" ry="200" fill="url(#blueLeaf)"/>
    <ellipse cx="540" cy="90" rx="170" ry="150" fill="url(#redBloomTop)"/>
    <ellipse cx="230" cy="620" rx="230" ry="200" fill="url(#warmBloom)"/>
    <ellipse cx="230" cy="900" rx="200" ry="160" fill="url(#orangeBloom)"/>
  </svg>

  <h1>
    <span class="title title-line-one">BRIGHT</span>
    <span class="title title-line-two">PATH</span>
  </h1>

  <p class="subtitle-band subtitle-primary">UNLOCKING THE GOLDEN KEY</p>
  <p class="subtitle-band subtitle-secondary">FOR VIGOR &amp; CONTENTMENT</p>

  <p class="author-name">MARTIN R. VELLACOTT</p>
  <p class="author-credentials">HYDRATION EXPERT &amp; CERTIFIED NUTRITIONAL THERAPIST</p>
</main>
</body>
</html>
```